Personal training and nutrition business needs business card design

We need a business card that outlays our services and invites potential customers to join our team and take the first step to a healthier and more enjoyable life. We cater for any level of fitness and specialize in weight loss and conditioning, strength training, muscle gain and strength endurance. Whether you are just starting off or need some help getting to the next level of your journey we are here to get the job done.
We specialize in one on one or one on two personal training sessions and each program will be custom made to suit individual fitness goals of our clients

```html
<!DOCTYPE html>
<html lang="en">
<head>
<meta charset="utf-8">
<title>Stride &amp; Sway — Business Card</title>
<link href="https://fonts.googleapis.com/css2?family=Roboto:wght@400;700;900&family=Oswald:wght@500&family=Exo+2:ital,wght@1,800&display=swap" rel="stylesheet">
<style>
  :root {
    --backdrop: #2b2b2b;
    --card: #ececec;
    --ink: #111111;
    --text: #2a2a2a;
    --purple: #7a3fa8;
    --violet: #5b3a9c;
    --orchid: #a24fa6;
    --black: #050505;
    --white: #ffffff;
  }
  * { box-sizing: border-box; margin: 0; padding: 0; }
  html, body { width: 1200px; height: 1138px; overflow: hidden; }
  body {
    background: var(--backdrop);
    position: relative;
    font-family: "Roboto", sans-serif;
  }
  .card {
    position: absolute;
    width: 620px;
    height: 376px;
    border-radius: 14px;
    background: linear-gradient(160deg, #f2f2f2, #e2e2e2);
    overflow: hidden;
  }
  /* Front */
  .card-front { left: 274px; top: 186px; }
  .front-brand {
    position: absolute;
    top: 138px;
    left: 0; right: 0;
    display: flex;
    justify-content: center;
    align-items: center;
    gap: 14px;
  }
  .brand-dot {
    width: 22px; height: 22px;
    border-radius: 50%;
    background: var(--purple);
  }
  .brand-name {
    font-family: "Roboto", sans-serif;
    font-weight: 900;
    font-size: 46px;
    letter-spacing: 2px;
    color: var(--ink);
  }
  .tagline {
    font-family: "Oswald", sans-serif;
    font-weight: 500;
    color: var(--orchid);
    letter-spacing: 1px;
    text-transform: uppercase;
  }
  .front-tagline {
    position: absolute;
    top: 252px;
    left: 0; right: 0;
    text-align: center;
    font-size: 14px;
  }
  .front-web {
    position: absolute;
    top: 322px;
    left: 0; right: 0;
    display: flex;
    justify-content: center;
    align-items: center;
    gap: 18px;
    font-size: 16px;
    color: var(--ink);
  }
  .rule { width: 72px; height: 2px; background: var(--ink); border-radius: 2px; }
  .front-band {
    position: absolute;
    left: 0; right: 0; bottom: 0;
    height: 9px;
    background: linear-gradient(90deg, var(--orchid), var(--violet));
  }
  /* Back */
  .card-back { left: 276px; top: 607px; }
  .back-curve { position: absolute; inset: 0; }
  .person-name {
    position: absolute;
    left: 38px; top: 82px;
    font-family: "Exo 2", sans-serif;
    font-style: italic;
    font-weight: 800;
    font-size: 26px;
    letter-spacing: 1px;
    color: var(--violet);
  }
  .person-role {
    position: absolute;
    left: 38px; top: 116px;
    font-size: 16px;
    color: var(--text);
  }
  .contact-list {
    position: absolute;
    left: 38px; top: 166px;
    list-style: none;
  }
  .contact-list li {
    display: flex;
    align-items: center;
    gap: 16px;
    height: 24px;
    font-size: 16px;
    color: var(--text);
  }
  .contact-list svg { width: 15px; height: 15px; fill: var(--purple); }
  .address {
    position: absolute;
    left: 38px; top: 252px;
    font-size: 16px;
    line-height: 24px;
    color: var(--text);
  }
  .back-brand {
    position: absolute;
    left: 360px; top: 110px;
    width: 250px;
    display: flex;
    flex-direction: column;
    align-items: center;
  }
  .back-brand .brand-dot { margin-bottom: 22px; width: 28px; height: 28px; }
  .back-brand .brand-name {
    color: var(--white);
    font-size: 40px;
    line-height: 42px;
    text-align: center;
  }
  .back-tagline { margin-top: 10px; font-size: 10px; }
</style>
</head>
<body>

<section class="card card-front">
  <div class="front-brand">
    <span class="brand-dot"></span>
    <span class="brand-name">STRIDE &amp; SWAY</span>
  </div>
  <p class="tagline front-tagline">Personal Training.&nbsp; Nutrition. Motivation</p>
  <div class="front-web">
    <span class="rule"></span>
    <span>www.strideandsway.com</span>
    <span class="rule"></span>
  </div>
  <div class="front-band"></div>
</section>

<section class="card card-back">
  <svg class="back-curve" viewBox="0 0 620 376" preserveAspectRatio="none">
    <defs>
      <linearGradient id="edgeGradient" x1="0" y1="0" x2="0" y2="1">
        <stop offset="0" stop-color="#5b3a9c"/>
        <stop offset="1" stop-color="#a24fa6"/>
      </linearGradient>
    </defs>
    <path d="M380,0 C318,70 296,250 388,376 L620,376 L620,0 Z" fill="url(#edgeGradient)"/>
    <path d="M386,0 C326,72 306,250 402,376 L620,376 L620,0 Z" fill="#050505"/>
  </svg>

  <h1 class="person-name">MARCUS DALE</h1>
  <p class="person-role">Personal Trainer</p>
  <ul class="contact-list">
    <li>
      <svg viewBox="0 0 16 16"><path d="M3 2h3l1 4-2 1c1 2 2 3 4 4l1-2 4 1v3c0 1-1 1-1 1C7 14 2 9 2 3c0 0 0-1 1-1z"/></svg>
      <span>+12 (555) 014-2290</span>
    </li>
    <li>
      <svg viewBox="0 0 16 16"><path d="M1 3h14v10H1z M2 4l6 5 6-5" fill="none" stroke="#7a3fa8" stroke-width="1.6"/></svg>
      <span>marcus@strideandsway.com</span>
    </li>
    <li>
      <svg viewBox="0 0 16 16"><circle cx="8" cy="8" r="6.5" fill="none" stroke="#7a3fa8" stroke-width="1.4"/><path d="M1.5 8h13M8 1.5c-3 3-3 10 0 13M8 1.5c3 3 3 10 0 13" fill="none" stroke="#7a3fa8" stroke-width="1.2"/></svg>
      <span>www.strideandsway.com</span>
    </li>
  </ul>
  <p class="address">482 Cedar Bend Road<br>Brookfield Texas 75010</p>

  <div class="back-brand">
    <span class="brand-dot"></span>
    <span class="brand-name">STRIDE<br>&amp; SWAY</span>
    <p class="tagline back-tagline">Personal Training.&nbsp; Nutrition. Motivation</p>
  </div>
</section>

</body>
</html>
```